Contemporary new French wine brand needs logo and series of label design

to design a new contemporary logo and series of labels for a new French wine brand. We hope to attract not just current French wine drinkers but new ones who may appreciate a less traditional and more modern style.

Reason: we are wanting to extend the project for a few days more to receive more submissions since we had fewer designs submitted than we were expecting, maybe because of the holidays.

Target Market(s)

people who follow the arts community (eg. music, theatre, visual/video arts, dance) --- all mature ages.

Industry/Entity Type

French Wine

Requirements
Must have
• a clear, memorable treatment for the name BRUMAIS with accompanying logo.
Nice to have
• embossing, matte/gloss refinement, tasteful foil stamping, coated stock for the whites to help the integrity of the paper in and out of ice buckets. A combo of say, three types of fonts; a semi custom font for the brand name Brumais and maybe a script and one other.
Should not have
• not traditional French

```html
<!DOCTYPE html>
<html lang="fr">
<head>
<meta charset="utf-8">
<title>Brumais – Val de Loire label series</title>
<link rel="stylesheet" href="https://fonts.googleapis.com/css2?family=Courier+Prime&family=Raleway:wght@300;400&display=swap">
<style>
  :root {
    --page: #f1f1ef;
    --label-light: #fbfbfb;
    --label-dark: #1b1b1b;
    --ink-dark: #1c1c1c;
    --ink-light: #f4f4f4;
    --gold: #b8893f;
    --gold-soft: #d1a65c;
    --edge: #dcdcdc;
  }
  * { box-sizing: border-box; margin: 0; padding: 0; }
  html, body { width: 1200px; height: 1000px; overflow: hidden; }
  body { background: var(--page); }

  .canvas {
    position: relative;
    width: 1200px;
    height: 1000px;
    overflow: hidden;
    display: flex;
    justify-content: center;
    align-items: center;
    gap: 40px;
  }

  .label {
    position: relative;
    width: 340px;
    height: 304px;
    background: var(--label-light);
    border: 1px solid var(--edge);
    box-shadow: 0 6px 18px rgba(0,0,0,0.08);
    color: var(--ink-dark);
    overflow: hidden;
  }
  .label--red {
    background: var(--label-dark);
    border-color: var(--label-dark);
    color: var(--ink-light);
  }

  .brand-seal {
    position: absolute;
    left: 16px;
    top: 30px;
    width: 170px;
    height: 170px;
    border: 2px solid var(--gold);
    border-radius: 50%;
    display: flex;
    align-items: center;
    justify-content: center;
    font-family: "Raleway", sans-serif;
    font-weight: 400;
    font-size: 22px;
    letter-spacing: 2px;
    color: var(--gold);
  }
  .label--red .brand-seal { border-color: var(--gold-soft); color: var(--gold-soft); }

  .identity {
    position: absolute;
    left: 164px;
    top: 176px;
    width: 166px;
  }
  .identity__rule {
    display: block;
    width: 166px;
    height: 2px;
    background: var(--gold);
    margin-bottom: 7px;
  }
  .label--red .identity__rule { background: var(--gold-soft); }

  .identity__name {
    font-family: "Raleway", sans-serif;
    font-weight: 400;
    font-size: 34px;
    letter-spacing: 0.5px;
    line-height: 1;
    text-align: right;
  }
  .identity__variety {
    font-family: "Courier Prime", monospace;
    font-size: 16px;
    color: var(--gold);
    text-align: right;
    margin-top: 6px;
    white-space: nowrap;
    direction: rtl;
  }
  .identity__variety span { direction: ltr; unicode-bidi: embed; }
  .label--red .identity__variety { color: var(--gold-soft); }
  .identity__region {
    font-family: "Raleway", sans-serif;
    font-weight: 400;
    font-size: 12px;
    letter-spacing: 0.5px;
    text-align: right;
    margin-top: 4px;
  }
</style>
</head>
<body>
<main class="canvas">

  <article class="label label--white">
    <div class="brand-seal">BRUMAIS</div>
    <div class="identity">
      <span class="identity__rule"></span>
      <h2 class="identity__name">BRUMAIS</h2>
      <p class="identity__variety"><span>Sauvignon Blanc</span></p>
      <p class="identity__region">VAL DE LOIRE</p>
    </div>
  </article>

  <article class="label label--white">
    <div class="brand-seal">BRUMAIS</div>
    <div class="identity">
      <span class="identity__rule"></span>
      <h2 class="identity__name">BRUMAIS</h2>
      <p class="identity__variety"><span>Muscadet ‘Sur Lie’</span></p>
      <p class="identity__region">VAL DE LOIRE</p>
    </div>
  </article>

  <article class="label label--red">
    <div class="brand-seal">BRUMAIS</div>
    <div class="identity">
      <span class="identity__rule"></span>
      <h2 class="identity__name">BRUMAIS</h2>
      <p class="identity__variety"><span>Cabernet Franc</span></p>
      <p class="identity__region">VAL DE LOIRE</p>
    </div>
  </article>

</main>
</body>
</html>
```